Real Estate For Sale Signage

I'm an independent agent in Lismore NSW Australia with high standards and looking for a catching 'For Sale'sign board.
I like classy, elegant, stylish and simple best.
My colours are red, white and black.
I don't have a logo or other font designs I need to stick to. I like the concept of a house or real estate design.
Before I created this project I played around on publisher and created the PDF attached. I'm not sold on it, but I don't mind the way the name has been layed out. Originally I had a white background with black & red font.
Fancy fonts for my name would be nice, but must not be busy.
Updates

Just wanted to advise that I have updated my brief and used the tools available to help get my ideas through.

Thank you for your work and time.

Kind regards
Delphine

Industry/Entity Type

Real Estate

Requirements
Must have
• For Sale
Delphine Marsk Real Estate (must stand out)
0491 572 306 (must stand out)
17 Tindale Crescent East Lismore
www.delphinemarskrealestate.example.au

```html
<!DOCTYPE html>
<html lang="en">
<head>
<meta charset="utf-8">
<title>Delphine Marsk Real Estate – For Sale Sign</title>
<link rel="stylesheet" href="https://fonts.googleapis.com/css2?family=Great+Vibes&family=Jost:wght@300;400&display=swap">
<style>
  :root {
    --brand-red: #c8122f;
    --brand-black: #000000;
    --brand-white: #ffffff;
    --pattern-red: #cc2240;
  }
  html, body {
    margin: 0;
    padding: 0;
    overflow: hidden;
    background: var(--brand-white);
  }
  .sign {
    position: relative;
    width: 849px;
    height: 1200px;
    overflow: hidden;
    background: var(--brand-red);
    font-family: "Jost", "Futura", sans-serif;
    font-weight: 300;
    color: var(--brand-white);
  }
  .sign__pattern {
    position: absolute;
    left: 269px;
    top: 0;
    width: 580px;
    height: 1200px;
    background: radial-gradient(circle at 60% 40%, var(--pattern-red), var(--brand-red) 75%);
  }
  .sign__band {
    position: absolute;
    left: 0;
    top: 0;
    width: 269px;
    height: 1200px;
    background: var(--brand-black);
  }
  .for-sale {
    position: absolute;
    left: 82px;
    top: 1172px;
    margin: 0;
    font-size: 114px;
    line-height: 1;
    font-weight: 300;
    letter-spacing: 2px;
    white-space: nowrap;
    transform: rotate(-90deg);
    transform-origin: 0 0;
  }
  .agent-name { margin: 0; font-weight: 300; }
  .agent-name__line {
    position: absolute;
    display: flex;
    align-items: baseline;
    white-space: nowrap;
    line-height: 1;
  }
  .agent-name__line--first { left: 40px; top: 28px; }
  .agent-name__line--last { left: 300px; top: 252px; }
  .agent-name__initial {
    font-family: "Great Vibes", cursive;
    font-weight: 400;
    line-height: 1;
    padding-right: 6px;
  }
  .agent-name__line--first .agent-name__initial { font-size: 210px; }
  .agent-name__line--last .agent-name__initial { font-size: 170px; }
  .agent-name__rest {
    font-size: 104px;
    line-height: 1;
    letter-spacing: 1px;
  }
  .agency-type {
    position: absolute;
    right: 26px;
    top: 446px;
    margin: 0;
    font-size: 53px;
    line-height: 1;
    letter-spacing: 3px;
    font-weight: 300;
  }
  .phone {
    position: absolute;
    right: 26px;
    top: 838px;
    margin: 0;
    font-size: 70px;
    line-height: 1;
    letter-spacing: 3px;
    font-weight: 300;
  }
  .office {
    position: absolute;
    right: 26px;
    top: 962px;
    margin: 0;
    text-align: right;
    font-style: normal;
    font-size: 34px;
    line-height: 45px;
    letter-spacing: 2px;
  }
  .website {
    position: absolute;
    right: 26px;
    top: 1140px;
    margin: 0;
    font-size: 30px;
    line-height: 1;
    letter-spacing: 3.2px;
  }
</style>
</head>
<body>
  <main class="sign">
    <div class="sign__pattern" role="img" aria-label="Faint repeating pattern of small house-in-circle motifs on red"></div>
    <div class="sign__band"></div>

    <p class="for-sale">For Sale With</p>

    <h1 class="agent-name">
      <span class="agent-name__line agent-name__line--first">
        <span class="agent-name__initial">D</span><span class="agent-name__rest">elphine</span>
      </span>
      <span class="agent-name__line agent-name__line--last">
        <span class="agent-name__initial">M</span><span class="agent-name__rest">arsk</span>
      </span>
    </h1>
    <p class="agency-type">REAL ESTATE</p>

    <p class="phone">0491 572 306</p>

    <address class="office">
      VISIT<br>
      17 TINDALE CRES<br>
      EAST LISMORE NSW
    </address>

    <p class="website">delphinemarskrealestate.example.au</p>
  </main>
</body>
</html>
```